Business Card / Appointment Card for Physician

On one side it should give the logo, address, and contact information, and on the other side it should br an Appointment card.

One Side:
Logo (see attached files)
Board Certified American Orthopedic Surgery

1487 Harrowgate Ave.
Suite KM7
Bronx, NY 10527
Tel: (718) 552 - 1948
Fax: (718) 552 - 7210

628 Fourth Ave.
Suite 42
New York, NY 10087
Tel: (212) 734 - 2815

Second Side:
Appointment
give them a choice of Bronx or Mahattan office
For:
Date:
Time:

If you are unable to keep your appointment, please call (718) 263-5102 24hrs in advance.

Target Market(s)

People that need orthopedic surgery

Industry/Entity Type

Business

Contact Information for Business Card

smart and attractive

Requirements
Must have
• logo
• contact information on one side, appointment information on the other

```html
<!DOCTYPE html>
<html lang="en">
<head>
<meta charset="utf-8">
<title>Daniel R. Holloway MD PC – Business &amp; Appointment Card</title>
<link href="https://fonts.googleapis.com/css2?family=Source+Sans+3:wght@400;600;700&display=swap" rel="stylesheet">
<style>
  :root {
    --stage: #111111;
    --card: #ffffff;
    --navy: #24527f;
    --navy-dark: #1d3f63;
    --green: #63a346;
    --ink: #2b2b2b;
    --rule: #1a1a1a;
  }
  * { box-sizing: border-box; margin: 0; padding: 0; }
  html, body {
    width: 1200px; height: 1000px; overflow: hidden;
    background: var(--stage);
    font-family: "Source Sans 3", "Myriad Pro", Arial, sans-serif;
  }
  .stage {
    position: relative; width: 1200px; height: 1000px;
    display: flex; align-items: center; justify-content: center; gap: 50px;
  }
  .card {
    position: relative; width: 525px; height: 300px;
    background: var(--card); border-radius: 22px; overflow: hidden;
  }

  /* Front */
  .brand {
    position: absolute; top: 48px; left: 0; right: 0;
    display: flex; flex-direction: column; align-items: center;
  }
  .brand-row { display: flex; align-items: center; gap: 12px; }
  .brand-dot { width: 34px; height: 34px; border-radius: 50%; background: var(--navy); }
  .brand-name {
    font-size: 26px; font-weight: 700; color: var(--navy);
    letter-spacing: 0.3px; text-transform: uppercase;
  }
  .brand-tagline {
    margin-top: 2px; font-size: 12.5px; font-weight: 700; color: var(--navy);
    text-transform: uppercase; letter-spacing: 0.4px;
  }
  .offices {
    position: absolute; top: 150px; left: 40px; right: 40px;
    display: grid; grid-template-columns: 1fr 70px 1fr; align-items: center;
  }
  .office { font-size: 15px; line-height: 1.3; color: var(--navy); }
  .office--bronx { text-align: right; }
  .office .contact { color: var(--green); font-weight: 700; }
  .divider {
    display: flex; flex-direction: column; align-items: center; gap: 6px;
  }
  .divider-line { width: 2px; height: 22px; background: var(--navy); }
  .home-badge {
    width: 36px; height: 36px; border-radius: 50%; background: var(--navy);
    display: flex; align-items: center; justify-content: center;
  }

  /* Back */
  .appt-band {
    position: absolute; top: 0; left: 0; right: 0; height: 112px;
    background: var(--green); color: #fff;
    display: flex; align-items: flex-end; justify-content: space-between;
    padding: 0 30px 18px 28px;
  }
  .appt-title { font-size: 44px; font-weight: 700; line-height: 1; }
  .office-choice { display: flex; gap: 24px; font-size: 14px; font-weight: 600; text-transform: uppercase; }
  .choice { display: flex; align-items: center; gap: 8px; }
  .choice-box { width: 20px; height: 20px; background: #fff; }
  .appt-fields {
    position: absolute; top: 140px; left: 70px; right: 60px;
    display: flex; flex-direction: column; gap: 10px;
  }
  .field { display: flex; align-items: flex-end; gap: 14px; }
  .field-label { width: 48px; font-size: 18px; font-weight: 700; color: var(--navy); text-align: right; }
  .field-line { flex: 1; border-bottom: 1.5px solid var(--rule); height: 20px; }
  .appt-note {
    position: absolute; bottom: 22px; left: 28px; right: 20px;
    font-size: 13px; font-weight: 700; color: var(--ink);
  }
  .appt-note .phone { color: var(--green); }
</style>
</head>
<body>
<main class="stage">
  <section class="card card--front" aria-label="Business card">
    <div class="brand">
      <div class="brand-row">
        <span class="brand-dot"></span>
        <span class="brand-name">Daniel R. Holloway MD PC</span>
      </div>
      <span class="brand-tagline">Orthopaedic Surgery &amp; Sports Medicine</span>
    </div>
    <div class="offices">
      <address class="office office--bronx" style="font-style:normal">
        1487 Harrowgate Ave.<br>
        Suite KM7, Bronx, NY 10527<br>
        <span class="contact">Tel: (718) 552 - 1948</span><br>
        <span class="contact">Fax: (718) 552 - 7210</span>
      </address>
      <div class="divider">
        <span class="divider-line"></span>
        <span class="home-badge">
          <svg width="20" height="20" viewBox="0 0 20 20" aria-hidden="true">
            <path d="M10 2 L19 10 H16 V18 H12 V13 H8 V18 H4 V10 H1 Z" fill="#fff"/>
          </svg>
        </span>
        <span class="divider-line"></span>
      </div>
      <address class="office office--manhattan" style="font-style:normal; padding-left:8px">
        628 Fourth Ave.<br>
        Suite 42<br>
        New York, NY 10087<br>
        <span class="contact">Tel: (212) 734 - 2815</span>
      </address>
    </div>
  </section>

  <section class="card card--back" aria-label="Appointment card">
    <header class="appt-band">
      <h1 class="appt-title">Appointment</h1>
      <div class="office-choice">
        <span class="choice">Bronx <span class="choice-box"></span></span>
        <span class="choice">Mahattan <span class="choice-box"></span></span>
      </div>
    </header>
    <div class="appt-fields">
      <div class="field"><span class="field-label">FOR</span><span class="field-line"></span></div>
      <div class="field"><span class="field-label">Date</span><span class="field-line"></span></div>
      <div class="field"><span class="field-label">Time</span><span class="field-line"></span></div>
    </div>
    <p class="appt-note">If you are unable to keep your appointment, Please call <span class="phone">(718) 263-5102</span> 24hrs in advance</p>
  </section>
</main>
</body>
</html>
```